business card design for heron textile printing

Heron Textile Printing requires elegant and colorful designs for its business card, ensuring both are visually cohesive and reflect the brand’s creative, modern identity. The logo is already finalized and should be a central element in designs.

## Business Card Design Brief

- Feature the logo clearly, with colors and style matching the letterhead.
- Present contact information (name, title, phone, email, website, address) in a clear, organized manner.
- Open to creative layouts, finishes, and double-sided designs, as long as the card remains professional and easy to read.
- Ensure both pieces feel unified as part of the same brand identity.

The final designs should be vibrant, professional, and memorable, showcasing Heron Textile Printing’s creative spirit.

Target Market(s)

Pakistan

Industry/Entity Type

Textile printing

Other font styles liked:
• Calibri

Requirements
Must have
• Address Email Address Phone number designer can ask me when start designing

```html
<!DOCTYPE html>
<html lang="en">
<head>
<meta charset="utf-8">
<title>Heron Textile Printing – Stationery</title>
<link href="https://fonts.googleapis.com/css2?family=Open+Sans:wght@400;600;700&family=Lato:wght@300;400&display=swap" rel="stylesheet">
<style>
  :root {
    --backdrop: #e4e4e4;
    --paper: #ffffff;
    --brand-maroon: #5b1d1d;
    --brand-orange: #f47a20;
    --ink: #222222;
    --ink-soft: #555555;
    --signature-tone: #d9d9de;
  }
  * { margin: 0; padding: 0; box-sizing: border-box; }
  html, body { width: 1200px; height: 933px; overflow: hidden; }
  body { background: var(--backdrop); font-family: "Open Sans", Calibri, sans-serif; color: var(--ink); position: relative; }

  .letterhead, .business-card { position: absolute; background: var(--paper); }

  /* Letterhead */
  .letterhead { left: 98px; top: 53px; width: 550px; height: 777px; }
  .wordmark { position: absolute; color: var(--brand-maroon); font-weight: 700; line-height: 1; font-family: "Open Sans", Calibri, sans-serif; }
  .wordmark .name-main { display: block; }
  .wordmark .name-sub { display: block; letter-spacing: 0.12em; }
  .brand-dot { position: absolute; border-radius: 50%; background: var(--brand-orange); }

  .letterhead .wordmark { left: 52px; top: 128px; text-align: center; }
  .letterhead .wordmark .name-main { font-size: 17px; }
  .letterhead .wordmark .name-sub { font-size: 6px; margin-top: 2px; }
  .letterhead .brand-dot { left: 72px; top: 76px; width: 46px; height: 46px; }

  .contact-block { position: absolute; left: 369px; top: 30px; padding-left: 15px; border-left: 1.2px solid var(--brand-orange); font-size: 10px; line-height: 14px; }
  .contact-block .address { margin-bottom: 6px; }
  .contact-line { display: flex; align-items: center; gap: 4px; }
  .contact-line svg { width: 7px; height: 7px; fill: var(--brand-orange); flex: none; }

  .recipient { position: absolute; left: 52px; top: 181px; font-family: "Lato", sans-serif; color: var(--ink-soft); }
  .recipient .recipient-name { font-size: 11px; font-weight: 400; }
  .recipient .recipient-line { font-size: 8px; line-height: 13.5px; }

  .letter-body { position: absolute; left: 52px; top: 276px; width: 446px; font-family: "Lato", sans-serif; font-size: 8px; line-height: 13.5px; color: var(--ink-soft); text-align: justify; }
  .letter-body p + p { margin-top: 11.5px; }

  .sign-off { position: absolute; left: 52px; top: 574px; font-family: "Lato", sans-serif; color: var(--ink-soft); }
  .sign-off .closing { font-size: 8.5px; }
  .signature-area { width: 66px; height: 17px; margin: 6px 0 4px; background: var(--signature-tone); border-radius: 3px; }
  .sign-off .signer { font-size: 10.5px; }

  /* Business cards */
  .business-card { left: 757px; width: 343px; height: 196px; }
  .card-front { top: 378px; }
  .card-back { top: 601px; }

  .card-front .wordmark { left: 11px; top: 11px; text-align: center; }
  .card-front .wordmark .name-main { font-size: 27px; }
  .card-front .wordmark .name-sub { font-size: 10px; margin-top: 2px; }
  .card-front .brand-dot { left: 175px; top: 40px; width: 130px; height: 130px; }

  .card-holder { position: absolute; left: 11px; top: 71px; }
  .card-holder .holder-name { color: var(--brand-orange); font-weight: 600; font-size: 16px; line-height: 20px; }
  .card-holder .holder-title { font-size: 9.5px; }
  .card-contacts { position: absolute; left: 12px; top: 111px; font-size: 9px; line-height: 13.5px; }
  .card-contacts .address { margin-bottom: 7px; }

  .card-back .brand-dot { left: 129px; top: 30px; width: 86px; height: 86px; }
  .card-back .wordmark { left: 0; right: 0; top: 134px; text-align: center; }
  .card-back .wordmark .name-main { font-size: 23px; }
  .card-back .wordmark .name-sub { font-size: 9px; margin-top: 2px; }
</style>
</head>
<body>

<svg width="0" height="0" style="position:absolute">
  <symbol id="icon-phone" viewBox="0 0 10 10"><path d="M1 3 Q5 0 9 3 L8 4.5 L6.5 3.8 L6.5 3 Q5 2.5 3.5 3 L3.5 3.8 L2 4.5 Z M2.5 5 H7.5 L8.5 9 H1.5 Z"/></symbol>
  <symbol id="icon-mail" viewBox="0 0 10 10"><path d="M0.5 2 H9.5 V8 H0.5 Z M1 2.5 L5 5.5 L9 2.5" stroke="#fff" stroke-width="0.8"/></symbol>
  <symbol id="icon-globe" viewBox="0 0 10 10"><circle cx="5" cy="5" r="4.5"/><path d="M5 0.5 V9.5 M0.5 5 H9.5 M5 0.5 Q2 5 5 9.5 M5 0.5 Q8 5 5 9.5" stroke="#fff" stroke-width="0.6" fill="none"/></symbol>
</svg>

<section class="letterhead" aria-label="Letterhead">
  <span class="brand-dot"></span>
  <div class="wordmark">
    <span class="name-main">HERON</span>
    <span class="name-sub">TEXTILE PRINTING</span>
  </div>

  <div class="contact-block">
    <div class="address">Your address, City<br>State, Zip 1234</div>
    <div class="contact-line"><svg><use href="#icon-phone"/></svg>123 456 789</div>
    <div class="contact-line"><svg><use href="#icon-mail"/></svg>info@yourgmail.com</div>
    <div class="contact-line"><svg><use href="#icon-globe"/></svg>www.yourwebsite.com</div>
  </div>

  <div class="recipient">
    <div class="recipient-name">AMARA QURESHI</div>
    <div class="recipient-line">Chief Exective Officer</div>
    <div class="recipient-line">City/State, Zip Code</div>
  </div>

  <div class="letter-body">
    <p>Proin gravida nibh vel velit auctor aliquet. Aenean sollicitudin, lorem quis bibendum auctor, nisi elit consequat ipsum, nec sagittis sem nibh id elit. Duis sed odio sit amet nibh vulputate cursus a sit amet mauris. Morbi accumsan ipsum velit. Nam nec tellus a odio tincidunt auctor a ornare odio. Sed non mauris vitae erat consequat auctor eu in elit. Class aptent taciti sociosqu ad litora torquent ugue. Sed non neque elit. Sed ut imperdiet nisi. Proin condimentum fermentum nunc. Etiam pharetra, imperdiet nisi. Proin condimentum fermentum nunc. Etiam pharetra, erat sed fermentum feugiat, velit mauris egestas quam, ut aliquam massa nisl quis neque. Suspendisse in orci enim.</p>
    <p>This is Photoshop's version of Lorem Ipsum. Proin gravida nibh vel velit auctor aliquet. Aenean sollicitudin, lorem quis bibendum auctor, nisi elit consequat ipsum, nec sagittis sem nibh id elit. Duis sed odio sit amet nibh vulputate cursus a sit amet mauris. Mo rbi accumsan ipsum velit. Nam nec tellus a odio tincidunt auctor a ornare odio. Sed non mauris vitae erat consequat auctor eu in elit. Class aptt consequat auctor eu in elit. Class aptent taciti sociosqu ad litora torquent per conubia nostra, per inceptos himenaeos. Mauris in erat justo.</p>
    <p>Nullam ac urna eu felis dapibus condimentum sit amet a augue. Sed non neque elit. Sed ut imperdiet nisi. Proin condimentum fermentum nunc. Etiam pharetra, erat sed fermentum feugiat, velit mauris egestas quam.Nullam ac urna eu felis dapibus condimentum sit amet a aug pharetra, erat sed fermentum feugiat, velit mauris egestas quam.Nullam ac urna eu felis dapibus condimentum sit amet a augue. Sed non neque elit. Sed ut imperdiet nisi. Proin condimentum fermentum nunc.</p>
  </div>

  <div class="sign-off">
    <div class="closing">Sincerely,</div>
    <div class="signature-area" role="img" aria-label="Handwritten signature"></div>
    <div class="signer">Bilal Rahman</div>
  </div>
</section>

<section class="business-card card-front" aria-label="Business card front">
  <div class="wordmark">
    <span class="name-main">HERON</span>
    <span class="name-sub">TEXTILE PRINTING</span>
  </div>
  <span class="brand-dot"></span>

  <div class="card-holder">
    <div class="holder-name">BILAL RAHMAN</div>
    <div class="holder-title">Managing Director</div>
  </div>

  <div class="card-contacts">
    <div class="address">Your address, City<br>State, Zip 1234</div>
    <div class="contact-line"><svg><use href="#icon-phone"/></svg>123 456 789</div>
    <div class="contact-line"><svg><use href="#icon-mail"/></svg>info@yourgmail.com</div>
    <div class="contact-line"><svg><use href="#icon-globe"/></svg>www.yourwebsite.com</div>
  </div>
</section>

<section class="business-card card-back" aria-label="Business card back">
  <span class="brand-dot"></span>
  <div class="wordmark">
    <span class="name-main">HERON</span>
    <span class="name-sub">TEXTILE PRINTING</span>
  </div>
</section>

</body>
</html>
```